Healthcare Recruitment Agency Brochure

We need our current Brochure updated as its old and dated. The brochure will be for our current and potential Clients and should provide all the necessary information regarding our services, but in a well presented, easy reading format which echoes our company Brand. The company supplies Healthcare establishments with trained healthcare Staff which can be in a variety of settings.
UPDATE: Following the submission of many designs we would like to amend the information/content to be included in the brochure and have uploaded additional information. We would like an 8 page booklet with the various sections spread out so as not to look to 'wordy' page 1 Front cover, 2 About Us, 3 Our Service, 4 Our promise, 5 Our Staff, 6 Our Ethos, 7 What Our Clients Say/Testimonials, 8 Contact Us/Back page. Please if using pictures (which is welcomed) steer away from the surgical/doctor type. We mainly provide care to the Elderly within Nursing and Residential Homes and Support Environments. Thanks
Updates

Target Market(s)

Healthcare clientell

Industry/Entity Type

Healthcare

Requirements
Must have
• Pictures, animation, easy reading, informative, tie in with website theme www.carewellstaffline.example
Nice to have
• open to ideas
Should not have
• very long text paragraphs

```html
<!DOCTYPE html>
<html lang="en">
<head>
<meta charset="utf-8">
<title>Carewell Staffline – Brochure Spread</title>
<link href="https://fonts.googleapis.com/css2?family=Montserrat:wght@400;500;600&family=Open+Sans:wght@400;700&display=swap" rel="stylesheet">
<style>
  :root{
    --backdrop:#dcdcdc;
    --paper:#f7f7f8;
    --panel:#ececee;
    --ink:#3e3e44;
    --ink-soft:#6a6a72;
    --green:#1fa36b;
    --sky:#c7d6ea;
    --photo-light:#eef0f3;
    --photo-skin:#d9c3b6;
    --tag:#e8d36a;
  }
  *{box-sizing:border-box;margin:0;padding:0}
  html,body{width:1200px;height:840px;overflow:hidden;background:var(--backdrop)}
  .spread{position:absolute;left:40px;top:30px;width:1120px;height:780px;display:flex;box-shadow:0 10px 30px rgba(0,0,0,.18)}
  .page{position:relative;width:560px;height:780px;background:var(--paper);overflow:hidden;font-family:"Montserrat",sans-serif;color:var(--ink)}
  .page--left{border-right:1px solid #d8d8db;background:linear-gradient(90deg,var(--paper) 85%,#e6e6e9)}
  .page--right{background:linear-gradient(90deg,#e8e8eb,var(--paper) 12%)}

  .photo{position:absolute}
  .photo--team-top{left:60px;top:40px;width:340px;height:270px;background:linear-gradient(135deg,var(--photo-skin),var(--photo-light) 70%)}
  .photo--team-side{left:410px;top:300px;width:100px;height:150px;background:linear-gradient(180deg,var(--photo-light),var(--photo-skin))}

  .brand{position:absolute;left:330px;top:110px;display:flex;align-items:center;gap:8px;font-size:17px;font-weight:500;color:#5b7fb0}
  .brand__dot{width:12px;height:12px;border-radius:50%;background:#5b7fb0}

  .about{position:absolute;left:95px;top:210px;width:330px;height:370px;background:var(--panel);padding:48px 34px 0;text-align:center}
  .about__title{font-size:27px;font-weight:500;letter-spacing:1px;margin-bottom:22px}
  .about__title span{color:var(--green)}
  .about p{font-size:9.5px;line-height:1.6;margin-bottom:10px;color:var(--ink-soft)}
  .about strong{color:var(--ink);font-weight:600}

  .rule--bottom{position:absolute;left:60px;top:700px;width:280px;height:4px;background:var(--green)}
  .folio{position:absolute;top:745px;font-size:8px;padding:1px 5px;border:1px solid var(--tag);color:var(--ink-soft)}
  .folio--left{left:30px}
  .folio--right{right:30px}

  .photo-backdrop{position:absolute;left:40px;top:150px;width:250px;height:460px;background:var(--sky)}
  .photo--nurses{left:70px;top:70px;width:240px;height:580px;background:linear-gradient(180deg,var(--photo-skin) 0%,#e9eef5 30%,#f4f6f9 100%)}

  .promise{position:absolute;left:320px;top:140px;width:200px}
  .promise__lead{font-family:"Open Sans",sans-serif;font-weight:700;font-size:9.5px;line-height:1.45;margin-bottom:14px;color:#222}
  .promise__list{list-style:none}
  .promise__list li{font-size:7.6px;line-height:1.55;color:var(--ink-soft);margin-bottom:9px}
  .promise__list li::before{content:"· "}
  .rule--side{position:absolute;left:532px;top:260px;width:5px;height:400px;background:var(--green)}
</style>
</head>
<body>
<main class="spread">
  <section class="page page--left">
    <div class="photo photo--team-top" role="img" aria-label="Care team joining hands together in the air"></div>
    <div class="photo photo--team-side" role="img" aria-label="Smiling care workers looking up"></div>
    <div class="brand"><span class="brand__dot"></span>Carewell Staffline</div>
    <article class="about">
      <h2 class="about__title">ABOUT <span>US</span></h2>
      <p>With over 15 years of experience <strong>Carewell Staffline</strong> specialises in reliable recruitment solutions for the healthcare sector.</p>
      <p>We are RSA accredited so you can rest assured that we will always be working in line with current legislation and guidelines.</p>
      <p>We strive for excellence in every aspect of our service, this includes ensuring that we are always fair, honest, and supportive of our temporary staff members, which is why we are a National Living Wage Employer.</p>
    </article>
    <div class="rule--bottom"></div>
    <span class="folio folio--left">2</span>
  </section>

  <section class="page page--right">
    <div class="photo-backdrop"></div>
    <div class="photo photo--nurses" role="img" aria-label="Group of care staff in uniforms raising hands together"></div>
    <article class="promise">
      <p class="promise__lead">We know that our Clients often have a lot on their plate, which is why we pride ourselves on being extremely accommodating:</p>
      <ul class="promise__list">
        <li>We can visit you at a time to suit you, to discuss your requirements and our service.</li>
        <li>We will give you our client application pack including everything you need to know, to start booking staff from Carewell Staffline we simply need a completed client account form.</li>
        <li>We have staff available to work at the drop of a hat, we understand the need for urgency and will make it our mission to try to help you every time.</li>
        <li>Our friendly office staff will always be at the end of the phone to deal with your requests; we never outsource to call centres.</li>
        <li>We will never leave you waiting and always be honest and realistic in telling you whether we can help.</li>
        <li>When you have booked a staff member you will always receive their compliance form, in a format that suits you.</li>
        <li>You can choose how frequently and in which format we send you your staff rotas, we will be completely flexible to your needs.</li>
        <li>We are always interested in how we could improve, we will regularly review our service and come and visit you when requested.</li>
        <li>We will regularly send you monitoring forms so you can quickly and easily pass on your feedback about the staff members we are sending you.</li>
      </ul>
    </article>
    <div class="rule--side"></div>
    <span class="folio folio--right">3</span>
  </section>
</main>
</body>
</html>
```